Veltrano - Mechanic/Collision Center Business Card

We're looking for a business card design for our mechanic/ collision repair shop.

Can be with colours or monochromatic.

See the attached files.

Many thanks

```html
<!DOCTYPE html>
<html lang="en">
<head>
<meta charset="utf-8">
<title>Veltrano – Business Card</title>
<link rel="stylesheet" href="https://fonts.googleapis.com/css2?family=Montserrat:wght@400;500;700;800&display=swap">
<style>
  :root {
    --page: #e9e6e2;
    --card-dark: #1b1e21;
    --brand-blue: #2a9ad8;
    --text-light: #f2f2f2;
    --rule-grey: #6b6e72;
    --white: #ffffff;
  }
  * { margin: 0; padding: 0; box-sizing: border-box; }
  html, body {
    width: 1200px; height: 909px; overflow: hidden;
    background: var(--page);
    font-family: "Montserrat", sans-serif;
  }
  .canvas { position: relative; width: 1200px; height: 909px; }

  .card {
    position: absolute;
    width: 700px; height: 400px;
    border-radius: 26px;
    background: var(--card-dark);
    overflow: hidden;
    box-shadow: 0 6px 18px rgba(0,0,0,.18);
  }
  .card--front { left: 70px; top: 36px; }
  .card--back  { left: 430px; top: 473px; }

  /* brand wordmark */
  .wordmark {
    display: flex; align-items: center; gap: 14px;
    font-weight: 800; letter-spacing: 2px; text-transform: uppercase;
  }
  .wordmark__dot { width: 34px; height: 34px; border-radius: 50%; background: var(--brand-blue); }

  /* front */
  .front__brand {
    position: absolute; top: 110px; left: 0; right: 0;
    justify-content: center; color: var(--white); font-size: 46px;
  }
  .front__name {
    position: absolute; top: 218px; left: 0; right: 0; text-align: center;
    color: var(--brand-blue); font-weight: 700; font-size: 26px; letter-spacing: 1px;
  }
  .front__rule {
    position: absolute; top: 262px; left: 310px; width: 80px; height: 2px;
    background: var(--rule-grey);
  }
  .front__phone {
    position: absolute; top: 288px; left: 0; right: 0; text-align: center;
    color: var(--text-light); font-size: 17px;
  }

  /* back */
  .back__ring {
    position: absolute; left: 378px; top: -96px;
    width: 440px; height: 440px; border-radius: 50%;
    background: var(--brand-blue);
  }
  .back__disc {
    position: absolute; left: 390px; top: -108px;
    width: 440px; height: 440px; border-radius: 50%;
    background: var(--white);
  }
  .back__brand {
    position: absolute; left: 440px; top: 128px;
    color: var(--card-dark); font-size: 34px;
  }
  .back__brand .wordmark__dot { width: 26px; height: 26px; }

  .back__company {
    position: absolute; left: 48px; top: 64px;
    color: var(--brand-blue); font-weight: 700; font-size: 30px; letter-spacing: .5px;
  }
  .back__role {
    position: absolute; left: 50px; top: 108px;
    color: var(--text-light); font-size: 16px; font-weight: 500;
  }
  .back__role-rule {
    position: absolute; left: 50px; top: 136px; width: 88px; height: 3px;
    background: var(--brand-blue);
  }
  .back__address {
    position: absolute; left: 50px; top: 178px;
    color: var(--text-light); font-size: 16px; line-height: 1.55;
  }
  .contacts {
    position: absolute; left: 50px; top: 262px;
    list-style: none; color: var(--text-light); font-size: 16px;
  }
  .contacts__item { display: flex; align-items: center; gap: 14px; height: 34px; }
  .contacts__note { font-size: 10px; margin-left: 4px; }
  .contacts__icon {
    width: 22px; height: 22px; border-radius: 4px; background: var(--brand-blue);
    display: flex; align-items: center; justify-content: center; flex: none;
  }
</style>
</head>
<body>
<main class="canvas">

  <section class="card card--front" aria-label="Business card front">
    <div class="wordmark front__brand"><span class="wordmark__dot"></span>Veltrano</div>
    <p class="front__name">Rui Matos</p>
    <div class="front__rule"></div>
    <p class="front__phone">+351 912345670 (or just 912345670)</p>
  </section>

  <section class="card card--back" aria-label="Business card back">
    <div class="back__ring"></div>
    <div class="back__disc"></div>
    <div class="wordmark back__brand"><span class="wordmark__dot"></span>Veltrano</div>

    <h1 class="back__company">Veltrano, LDA</h1>
    <p class="back__role">Director</p>
    <div class="back__role-rule"></div>

    <address class="back__address" style="font-style:normal">
      Rua das Oficinas, 14<br>
      Postal code: 1000-123 Lisboa
    </address>

    <ul class="contacts">
      <li class="contacts__item">
        <span class="contacts__icon">
          <svg width="14" height="14" viewBox="0 0 24 24" aria-hidden="true"><path fill="#fff" d="M6.6 10.8a15 15 0 0 0 6.6 6.6l2.2-2.2c.3-.3.7-.4 1-.2 1.1.4 2.3.6 3.6.6.6 0 1 .4 1 1V20c0 .6-.4 1-1 1A17 17 0 0 1 3 4c0-.6.4-1 1-1h3.5c.6 0 1 .4 1 1 0 1.3.2 2.5.6 3.6.1.3 0 .7-.2 1z"/></svg>
        </span>
        <span>+351 210457890<span class="contacts__note">(or just 210457890)</span></span>
      </li>
      <li class="contacts__item">
        <span class="contacts__icon">
          <svg width="14" height="14" viewBox="0 0 24 24" aria-hidden="true"><rect x="3" y="5" width="18" height="14" rx="1.5" fill="none" stroke="#fff" stroke-width="2"/><path d="M3.5 6l8.5 7 8.5-7" fill="none" stroke="#fff" stroke-width="2"/></svg>
        </span>
        <span>veltrano.mail@postbox.pt</span>
      </li>
      <li class="contacts__item">
        <span class="contacts__icon"></span>
        <span>www.veltrano.pt</span>
      </li>
    </ul>
  </section>

</main>
</body>
</html>
```